I would like a single page website for Kestrel Lift Rentals. In the file list provided there is basic information to be included as well as our logo with colors, fonts and images to be included.
Site must be very simple and be able to be loaded onto smart phones etc very quickly.
Site needs to be very smart in appearance

Target Market(s)

All prospective drone customers from Police to Parties.

Industry/Entity Type

Hire

Coding

Coded - Design and coding required

Number of Pages Required

1 page

Requirements
Must have
• Must have variation of color schemes supplied
Nice to have
• Must be very eye catching without going over the top
Should not have
• Anything slow to load.

```html
<!DOCTYPE html>
<html lang="en">
<head>
<meta charset="utf-8">
<title>Kestrel Lift Rentals</title>
<link href="https://fonts.googleapis.com/css2?family=Roboto:wght@400;500;700&display=swap" rel="stylesheet">
<style>
:root{
  --navy:#2a2a8c;
  --navy-soft:#3a4a9a;
  --ink:#333;
  --muted:#555;
  --nav-active:#a6a6a6;
  --panel:#f4f4f4;
  --white:#fff;
  --sky-top:#3f6fb0;
  --sky-bottom:#5a86c2;
  --violet-a:#4b4cbc;
  --violet-b:#2e2a94;
  --night:#19213a;
  --footer:#f3f3f3;
}
*{margin:0;padding:0;box-sizing:border-box}
html,body{width:1200px;height:2380px;overflow:hidden;background:var(--white);font-family:'Roboto',Arial,sans-serif;color:var(--ink)}
.page{position:relative;width:1200px;height:2380px}

/* header */
.site-header{position:absolute;top:0;left:0;width:1200px;height:102px;background:var(--white)}
.brand{position:absolute;left:190px;top:34px;display:flex;align-items:center;gap:10px;font-weight:700;font-size:24px;color:var(--navy);letter-spacing:.5px}
.brand-dot{width:22px;height:22px;border-radius:50%;background:var(--navy)}
.main-nav{position:absolute;left:568px;top:0;height:102px;display:flex}
.main-nav a{display:flex;align-items:center;height:102px;padding:0 12px;font-size:13.5px;font-weight:700;color:var(--navy);text-decoration:none;white-space:nowrap}
.main-nav a.active{background:var(--nav-active);color:var(--white);padding:0 10px;margin-right:4px}

/* hero */
.hero{position:absolute;top:102px;left:0;width:1200px;height:362px;background:radial-gradient(ellipse at 62% 45%,#d9dde3 0,#b7c3d6 14%,var(--sky-bottom) 32%,var(--sky-top) 100%)}

/* about */
.about{position:absolute;top:464px;left:0;width:1200px;height:394px;background:var(--panel)}
.about-media{position:absolute;left:0;top:0;width:600px;height:394px;background:radial-gradient(ellipse at 45% 45%,#e8e8ec 0,#c9c9dc 16%,#4c48ad 38%,var(--violet-b) 100%)}
.about-body{position:absolute;left:626px;top:50px;width:372px}
.section-title{font-weight:400;font-size:29px;letter-spacing:.5px}
.about-body .section-title{color:var(--navy-soft);margin-left:3px}
.about-body p{margin-top:20px;font-size:11.4px;line-height:16.8px;color:#444}

/* products */
.products{position:absolute;top:858px;left:0;width:1200px;height:352px;background:var(--white)}
.products .section-title{position:absolute;top:47px;width:100%;text-align:center;color:var(--navy)}
.product-grid{position:absolute;left:192px;top:111px;display:flex;gap:19px}
.product-card{width:190px;height:190px;border:3px solid var(--navy);padding:14px;background:var(--white)}
.product-shot{width:100%;height:100%;background:radial-gradient(ellipse at 50% 55%,#d4d6da 0,#e9eaec 40%,#fff 75%)}

/* testimonials */
.testimonials{position:absolute;top:1210px;left:0;width:1200px;height:405px;background:linear-gradient(100deg,var(--violet-a),var(--violet-b))}
.testimonials .section-title{position:absolute;top:42px;width:100%;text-align:center;color:var(--white)}
.quote{position:absolute;width:460px;height:90px}
.quote-avatar{position:absolute;left:0;top:0;width:86px;height:86px;border-radius:50%;border:3px solid var(--white);background:linear-gradient(160deg,#c8ccd6,#3a3d56)}
.quote-text{position:absolute;left:105px;top:3px;width:275px;font-size:12.3px;line-height:20px;color:var(--white)}
.quote-name{position:absolute;left:105px;top:66px;font-size:17px;color:var(--white)}
.quote-company{position:absolute;left:105px;top:88px;font-size:10.5px;font-weight:700;color:var(--white)}

/* hire */
.hire{position:absolute;top:1615px;left:0;width:1200px;height:530px;background:radial-gradient(ellipse at 50% 55%,#2c3550 0,#1d2640 45%,var(--night) 100%)}
.hire .section-title{position:absolute;top:46px;width:100%;text-align:center;color:var(--white)}
.hire-form{position:absolute;left:359px;top:122px;width:482px}
.field{display:block;width:482px;height:47px;margin-bottom:13px;background:rgba(255,255,255,.4);border:1px solid rgba(255,255,255,.7);color:var(--white);font-family:'Roboto',Arial,sans-serif;font-size:14.5px;text-align:center;line-height:45px}
.field.message{height:153px;line-height:normal;padding-top:14px}
.submit{position:absolute;left:154px;top:303px;width:174px;height:45px;border:1px solid rgba(255,255,255,.8);background:transparent;color:var(--white);font-family:'Roboto',Arial,sans-serif;font-size:15px;font-weight:500;letter-spacing:.5px}

/* footer */
.site-footer{position:absolute;top:2145px;left:0;width:1200px;height:235px;background:var(--footer)}
.footer-col{position:absolute;top:40px}
.footer-col h3{font-size:14px;font-weight:400;color:var(--navy-soft);letter-spacing:.3px}
.link-list{list-style:none;margin-top:20px}
.link-list li{font-size:11.5px;line-height:22px;color:var(--ink)}
.contact-list{list-style:none;margin-top:20px}
.contact-list li{display:flex;gap:10px;font-size:11.5px;line-height:16px;color:var(--ink);margin-bottom:18px}
.contact-list svg{flex:none;margin-top:2px}
.footer-map{position:absolute;left:580px;top:44px;width:246px;height:140px;border:2px solid #d6d6d6;background:linear-gradient(135deg,#cfe0c4,#e9e4c9 45%,#b9cfe6)}
.social{display:flex;gap:10px;margin-top:18px}
.social span{width:30px;height:30px;border-radius:50%;border:2px solid var(--navy-soft)}
.copyright{margin-top:10px;font-size:11.5px;line-height:16.5px;color:var(--ink)}
</style>
</head>
<body>
<div class="page">

  <header class="site-header">
    <div class="brand"><span class="brand-dot"></span>Kestrel Lift Rentals</div>
    <nav class="main-nav">
      <a class="active" href="#">HOME</a>
      <a href="#">ABOUT US</a>
      <a href="#">OUR PRODUCTS</a>
      <a href="#">HIRE A DRONE</a>
      <a href="#">CONTACT US</a>
    </nav>
  </header>

  <section class="hero" role="img" aria-label="White quadcopter drone with camera flying against a blue sky"></section>

  <section class="about">
    <div class="about-media" role="img" aria-label="White quadcopter drone with camera gimbal on a deep blue background"></div>
    <div class="about-body">
      <h2 class="section-title">ABOUT US</h2>
      <p>Lorem ipsum dolor sit amet, consectetur adipiscing elit. Praesent at tincidunt dolor, nec pulvinar elit. Vivamus imperdiet ipsum lacus, eu suscipit lacus maximus sed. Donec a posuere magna. Fusce finibus, elit nec semper convallis, odio magna feugiat nibh, eget feugiat elit nunc eu erat. Vestibulum ante ipsum primis in faucibus orci luctus et ultrices posuere cubilia Curae; Aliquam ac ipsum in mi luctus bibendum ac vitae nibh. Cras malesuada consequat dui, efficitur ultrices lectus aliquam ut. Nulla congue sollicitudin suscipit. Phasellus luctus fringilla diam convallis elementum. Curabitur quis lobortis est. Proin venenatis luctus efficitur. Nam tempor mattis nibh, id hendrerit felis malesuada ac. Aliquam sit amet urna eu nulla eleifend bibendum sed ut est. Mauris tempus sodales nibh, eget scelerisque sem viverra sed.</p>
    </div>
  </section>

  <section class="products">
    <h2 class="section-title">OUR PRODUCTS</h2>
    <div class="product-grid">
      <div class="product-card"><div class="product-shot" role="img" aria-label="White camera drone product photo"></div></div>
      <div class="product-card"><div class="product-shot" role="img" aria-label="White camera drone product photo"></div></div>
      <div class="product-card"><div class="product-shot" role="img" aria-label="White camera drone product photo"></div></div>
      <div class="product-card"><div class="product-shot" role="img" aria-label="White camera drone product photo"></div></div>
    </div>
  </section>

  <section class="testimonials" aria-label="Testimonials">
    <h2 class="section-title">TESTIMONIALS</h2>
    <div class="quote" style="left:190px;top:112px">
      <div class="quote-avatar" role="img" aria-label="Customer portrait"></div>
      <p class="quote-text">Lorem ipsum dolor sit amet, consectetur adipiscing elit. Phasellus vel nibh auctor, ullamcorper tellus vel, feugiat tellus.</p>
      <div class="quote-name">Mr. Reed</div>
      <div class="quote-company">Lorem Ipsum Co.</div>
    </div>
    <div class="quote" style="left:632px;top:112px">
      <div class="quote-avatar" role="img" aria-label="Customer portrait"></div>
      <p class="quote-text">Lorem ipsum dolor sit amet, consectetur adipiscing elit. Phasellus vel nibh auctor, ullamcorper tellus vel, feugiat tellus.</p>
      <div class="quote-name">Mr. Reed</div>
      <div class="quote-company">Lorem Ipsum Co.</div>
    </div>
    <div class="quote" style="left:190px;top:261px">
      <div class="quote-avatar" role="img" aria-label="Customer portrait"></div>
      <p class="quote-text">Lorem ipsum dolor sit amet, consectetur adipiscing elit. Phasellus vel nibh auctor, ullamcorper tellus vel, feugiat tellus.</p>
      <div class="quote-name">Mr. Reed</div>
      <div class="quote-company">Lorem Ipsum Co.</div>
    </div>
    <div class="quote" style="left:632px;top:261px">
      <div class="quote-avatar" role="img" aria-label="Customer portrait"></div>
      <p class="quote-text">Lorem ipsum dolor sit amet, consectetur adipiscing elit. Phasellus vel nibh auctor, ullamcorper tellus vel, feugiat tellus.</p>
      <div class="quote-name">Mr. Reed</div>
      <div class="quote-company">Lorem Ipsum Co.</div>
    </div>
  </section>

  <section class="hire" role="img" aria-label="Dark close-up of a drone with propeller guards behind the hire form">
    <h2 class="section-title">HIRE A DRONE</h2>
    <form class="hire-form">
      <div class="field">Your Name</div>
      <div class="field">Your Email</div>
      <div class="field message">Your Message</div>
      <button class="submit" type="button">SUBMIT</button>
    </form>
  </section>

  <footer class="site-footer">
    <div class="footer-col" style="left:190px">
      <h3>IMPORTANT LINKS</h3>
      <ul class="link-list">
        <li>Home</li>
        <li>About Us</li>
        <li>Our Products</li>
        <li>Hire a Drone</li>
        <li>Contact Us</li>
      </ul>
    </div>
    <div class="footer-col" style="left:375px">
      <h3>CONTACT US</h3>
      <ul class="contact-list">
        <li><svg width="10" height="13" viewBox="0 0 10 13"><path d="M5 0a5 5 0 0 0-5 5c0 3.5 5 8 5 8s5-4.5 5-8a5 5 0 0 0-5-5zm0 7a2 2 0 1 1 0-4 2 2 0 0 1 0 4z" fill="#444"/></svg><span>Lorem Ipsum dolor Sit,<br>center.</span></li>
        <li><svg width="11" height="11" viewBox="0 0 11 11"><path d="M2.2 0l2 2.4-1 1.4a7 7 0 0 0 4 4l1.4-1L11 8.8 9.8 11C4.5 11 0 6.5 0 1.2z" fill="#444"/></svg><span>+61-400-555-018</span></li>
        <li><svg width="12" height="9" viewBox="0 0 12 9"><rect width="12" height="9" fill="#444"/><path d="M0 0l6 5 6-5" stroke="#f3f3f3" fill="none"/></svg><span>info@kestrelliftrentals.com</span></li>
      </ul>
    </div>
    <div class="footer-map" role="img" aria-label="Map showing the business location"></div>
    <div class="footer-col" style="left:865px">
      <h3>GET IN TOUCH</h3>
      <div class="social"><span></span><span></span><span></span></div>
      <p class="copyright">Copyright © 2014<br>Kestrel Lift Rentals.com.<br>All Rights Reserved</p>
    </div>
  </footer>

</div>
</body>
</html>
```